Real Estate Design Website

I would like to have a design for "real estate agent" website. It needs to be in a "Responsive" framework.

The design need to be suitable for different viewer from all around the world. It needs to be modern. It'd be great if there is a design for mobile and vexo/tablet (it's all under responsive framework). It needs to be easy to navigate and look modern

Target Market(s)

End user/Real estate buyers from different part of the world

Industry/Entity Type

Real Estate

Requirements
Must have
• It's for real estate agent website which is used to represent their brand/image but at the same time it also for their client which is real estate buyers
Should not have
• Should not be boring design/out of date

```html
<!DOCTYPE html>
<html lang="en">
<head>
<meta charset="utf-8">
<title>Real Estate</title>
<link rel="stylesheet" href="https://fonts.googleapis.com/css2?family=Open+Sans:wght@300;400;600;700&family=Arimo:wght@700&display=swap">
<style>
:root{
  --dark:#262626;
  --darker:#1c1c1c;
  --blue:#1a8ad0;
  --blue-dark:#137ab9;
  --red:#d9362a;
  --orange:#f07a50;
  --text:#2d2d2d;
  --muted:#555;
  --grey-band:#e9e8e6;
  --footer:#dedcd9;
  --line:#c9c9c9;
  --white:#fff;
}
*{margin:0;padding:0;box-sizing:border-box}
html,body{width:1200px;height:2429px;overflow:hidden}
body{font-family:"Open Sans",Arial,sans-serif;color:var(--text);background:var(--white);position:relative}
.block{position:absolute;left:0;width:1200px}
.wrap{position:absolute;left:131px;width:938px}

/* header */
.site-header{top:0;height:58px;background:var(--dark)}
.logo{position:absolute;left:131px;top:0;line-height:58px;color:var(--white);font-weight:700;font-size:19px;letter-spacing:.5px}
.main-nav{position:absolute;left:342px;top:0;display:flex;gap:28px;line-height:58px}
.main-nav a{color:var(--white);font-size:13.5px;text-decoration:none;font-weight:600}
.btn-register,.btn-login{position:absolute;top:12px;height:38px;line-height:38px;text-align:center;font-size:13px;color:var(--white);font-weight:600}
.btn-register{left:887px;width:92px;background:#383838}
.btn-login{left:994px;width:75px;background:var(--blue)}

/* hero */
.hero{top:58px;height:598px;background:linear-gradient(180deg,#5f7d55 0%,#8a9a86 30%,#b7b8ad 50%,#5a7b3e 80%,#3f6a2a 100%)}
.quick-search{position:absolute;left:790px;top:80px;width:279px;height:421px;background:rgba(215,215,215,.85);padding:18px 22px}
.quick-search h3{font-size:15px;font-weight:400;color:#333;letter-spacing:.5px;border-bottom:1px solid #aaa;padding-bottom:10px}
.qs-tabs{display:flex;justify-content:space-between;margin-top:20px;font-size:13px;color:var(--blue)}
.field{display:flex;height:30px;background:var(--white);margin-top:12px;font-size:12px;color:#333;align-items:center;padding-left:10px;position:relative}
.field::after{content:"";position:absolute;right:0;top:0;width:30px;height:30px;background:var(--blue)}
.field svg{position:absolute;right:9px;top:11px;z-index:1}
.qs-tabs+.field{margin-top:18px}
.field-row{display:flex;gap:12px}
.field-row .field{flex:1}
.btn-search{display:block;margin:14px 0 0 auto;width:104px;height:28px;line-height:28px;text-align:center;background:var(--blue);color:var(--white);font-size:13px}
.adv-link{display:block;text-align:right;margin-top:14px;font-size:13px;color:var(--blue)}

/* intro */
.intro{top:656px;height:165px;text-align:center}
.intro h1{font-family:"Arimo",Arial,sans-serif;font-size:39px;font-weight:700;color:#222;margin-top:30px}
.intro .rule{width:56px;height:3px;background:var(--blue);margin:18px auto 0}
.intro p{font-size:20px;color:#444;margin-top:12px}
.intro p span{color:var(--blue)}

/* listings */
.listings{top:821px;height:479px;background:var(--grey-band)}
.section-title{font-size:30px;font-weight:300;color:#222;letter-spacing:.5px}
.listings .section-title{position:absolute;left:131px;top:50px}
.cards{position:absolute;left:131px;top:110px;display:flex;gap:28px}
.card{width:213px;height:289px;background:var(--white);box-shadow:0 1px 3px rgba(0,0,0,.15);padding:9px}
.card .photo{height:128px}
.card h4{font-size:13px;font-weight:700;color:#444;margin-top:8px;padding-bottom:8px;border-bottom:1px solid #ddd}
.meta{display:grid;grid-template-columns:1fr 1fr;font-size:10.5px;color:#333;row-gap:14px;margin-top:10px}
.meta span{display:flex;align-items:center;gap:8px}
.meta svg{flex:none}
.card-foot{display:flex;align-items:center;margin-top:16px;border-top:1px solid #ddd;padding-top:8px}
.tag-sale{background:var(--blue);color:var(--white);font-size:12px;padding:0 9px;height:24px;line-height:24px}
.tag-plus{width:22px;height:22px;background:var(--orange);color:var(--white);margin-left:5px;text-align:center;line-height:22px;font-weight:700}
.price{margin-left:auto;color:var(--red);font-weight:700;font-size:20px}

/* agents */
.agents{top:1300px;height:390px}
.agents .section-title{position:absolute;left:131px;top:70px}
.agent{position:absolute;top:131px;height:234px;border:1px solid #d6d6d6;background:var(--white)}
.agent .portrait{position:absolute;left:19px;top:21px;width:180px;height:181px;border:1px solid #ccc}
.agent-info{position:absolute;left:222px;top:38px;width:220px}
.agent-info h4{font-size:16px;font-weight:700;color:#222}
.agent-info p{font-size:11px;line-height:16px;color:#333;margin-top:10px}
.agent-info .contact{margin-top:28px;font-size:10.5px;line-height:24px;font-weight:600}
.agent-info .contact em{font-style:normal;color:var(--red)}

/* services */
.services{top:1690px;height:376px}
.service{position:absolute;top:20px;width:290px;text-align:center}
.service .icon{width:100px;height:100px;border-radius:50%;background:#ececec;margin:0 auto;display:flex;align-items:center;justify-content:center}
.service .icon.active{background:#1f1f1f;box-shadow:0 0 0 5px var(--blue)}
.service h3{font-size:22px;font-weight:400;margin-top:20px;color:#222}
.service p{font-size:12px;line-height:15px;color:#333;margin-top:6px}
.btn-more{display:inline-block;margin-top:20px;background:var(--blue-dark);color:var(--white);font-size:11px;padding:4px 12px}

/* footer */
.site-footer{top:2066px;height:290px;background:var(--footer)}
.col{position:absolute;top:40px}
.col h5{font-size:15px;font-weight:400;color:#222;letter-spacing:.5px}
.links{list-style:none;margin-top:20px;width:220px}
.links li{font-size:11px;line-height:29px;border-bottom:1px solid #aaa;padding-left:14px;position:relative}
.links li::before{content:"";position:absolute;left:0;top:13px;width:4px;height:4px;background:#333;border-radius:50%}
.col p{font-size:11px;line-height:15px;color:#222;margin-top:20px}
.col .more{margin-top:14px}
.post{display:flex;gap:12px;margin-top:18px;width:210px}
.post .thumb{flex:none;width:62px;height:62px;border:2px solid var(--white)}
.post p{margin-top:2px;font-size:10.5px;line-height:13px}
.post small{display:block;font-size:9px;color:#555;margin-top:3px;font-style:italic}
.contact-list{list-style:none;margin-top:20px;font-size:11px;line-height:17px}
.contact-list li{display:flex;gap:14px;margin-bottom:14px}
.contact-list svg{flex:none;margin-top:2px}
.site-bottom{top:2356px;height:73px;background:var(--darker)}
.copyright{position:absolute;left:131px;top:0;line-height:73px;font-size:11.5px;color:var(--white)}
.social{position:absolute;left:928px;top:24px;display:flex;gap:11px}
.social span{width:25px;height:25px;background:#555}
.to-top{position:absolute;left:1110px;top:0;width:90px;height:73px;background:#3a3a3a;display:flex;align-items:center;justify-content:center}
</style>
</head>
<body>

<header class="block site-header">
  <div class="logo">REAL ESTATE</div>
  <nav class="main-nav">
    <a>HOME</a><a>SERVICES</a><a>HOME BUYERS</a><a>HOME SELLERS</a><a>TEAM</a><a>CONTACT</a>
  </nav>
  <div class="btn-register">REGISTER</div>
  <div class="btn-login">LOGIN</div>
</header>

<section class="block hero" role="img" aria-label="Photo of a two-storey suburban house with a red front door, green lawn and tall trees">
  <form class="quick-search">
    <h3>QUICK SEARCH</h3>
    <div class="qs-tabs"><span>For sale</span><span>For Rent</span></div>
    <div class="field">Location<svg width="12" height="8"><path d="M1 1l5 5 5-5" fill="none" stroke="#fff" stroke-width="2"/></svg></div>
    <div class="field">Property type<svg width="12" height="8"><path d="M1 1l5 5 5-5" fill="none" stroke="#fff" stroke-width="2"/></svg></div>
    <div class="field">Square Feet<svg width="12" height="8"><path d="M1 1l5 5 5-5" fill="none" stroke="#fff" stroke-width="2"/></svg></div>
    <div class="field-row">
      <div class="field">Beds<svg width="12" height="8"><path d="M1 1l5 5 5-5" fill="none" stroke="#fff" stroke-width="2"/></svg></div>
      <div class="field">Baths<svg width="12" height="8"><path d="M1 1l5 5 5-5" fill="none" stroke="#fff" stroke-width="2"/></svg></div>
    </div>
    <div class="field-row">
      <div class="field">Min price<svg width="12" height="8"><path d="M1 1l5 5 5-5" fill="none" stroke="#fff" stroke-width="2"/></svg></div>
      <div class="field">Max price<svg width="12" height="8"><path d="M1 1l5 5 5-5" fill="none" stroke="#fff" stroke-width="2"/></svg></div>
    </div>
    <span class="btn-search">Search</span>
    <span class="adv-link">Advanced Search</span>
  </form>
</section>

<section class="block intro">
  <h1>Lorem ipsum dolor sit amet, consectetur adipisicing elit,</h1>
  <div class="rule"></div>
  <p>Sed ut perspiciatis unde omnis iste natus error sit voluptatem <span>accusantium</span></p>
</section>

<section class="block listings">
  <h2 class="section-title">LATEST LISTINGS</h2>
  <div class="cards">
    <article class="card">
      <div class="photo" role="img" aria-label="Photo of a white house with an orange tiled roof" style="background:linear-gradient(180deg,#8fb5dc,#c9774e 45%,#e8e2d8 70%,#6a9a45)"></div>
      <h4>417 Linden Grove</h4>
      <div class="meta">
        <span><svg width="14" height="10"><rect x="1" y="4" width="12" height="5" fill="#666"/><rect x="1" y="1" width="4" height="3" fill="#666"/></svg>2 Bedrooms</span>
        <span><svg width="12" height="12"><rect x="1" y="1" width="10" height="10" fill="none" stroke="#666" stroke-width="1.5"/></svg>2198 sqft</span>
        <span><svg width="12" height="12"><path d="M1 6h10v3H1zM3 6V2h3" fill="none" stroke="#666" stroke-width="1.5"/></svg>4 baths</span>
        <span><svg width="14" height="10"><rect x="1" y="3" width="12" height="5" rx="2" fill="#666"/></svg>2 Car Garage</span>
      </div>
      <div class="card-foot"><span class="tag-sale">Fore Sale</span><span class="tag-plus">+</span><span class="price">$192,00</span></div>
    </article>
    <article class="card">
      <div class="photo" role="img" aria-label="Photo of a beige family house with a green garden" style="background:linear-gradient(180deg,#a9c4df,#6d6a5c 40%,#c9b993 65%,#5a8a3a)"></div>
      <h4>417 Linden Grove</h4>
      <div class="meta">
        <span><svg width="14" height="10"><rect x="1" y="4" width="12" height="5" fill="#666"/><rect x="1" y="1" width="4" height="3" fill="#666"/></svg>2 Bedrooms</span>
        <span><svg width="12" height="12"><rect x="1" y="1" width="10" height="10" fill="none" stroke="#666" stroke-width="1.5"/></svg>2198 sqft</span>
        <span><svg width="12" height="12"><path d="M1 6h10v3H1zM3 6V2h3" fill="none" stroke="#666" stroke-width="1.5"/></svg>4 baths</span>
        <span><svg width="14" height="10"><rect x="1" y="3" width="12" height="5" rx="2" fill="#666"/></svg>2 Car Garage</span>
      </div>
      <div class="card-foot"><span class="tag-sale">Fore Sale</span><span class="tag-plus">+</span><span class="price">$192,00</span></div>
    </article>
    <article class="card">
      <div class="photo" role="img" aria-label="Photo of a grey-roofed suburban house on a lawn" style="background:linear-gradient(180deg,#7fb0e0,#56606c 40%,#d8d4cc 65%,#5f9440)"></div>
      <h4>417 Linden Grove</h4>
      <div class="meta">
        <span><svg width="14" height="10"><rect x="1" y="4" width="12" height="5" fill="#666"/><rect x="1" y="1" width="4" height="3" fill="#666"/></svg>2 Bedrooms</span>
        <span><svg width="12" height="12"><rect x="1" y="1" width="10" height="10" fill="none" stroke="#666" stroke-width="1.5"/></svg>2198 sqft</span>
        <span><svg width="12" height="12"><path d="M1 6h10v3H1zM3 6V2h3" fill="none" stroke="#666" stroke-width="1.5"/></svg>4 baths</span>
        <span><svg width="14" height="10"><rect x="1" y="3" width="12" height="5" rx="2" fill="#666"/></svg>2 Car Garage</span>
      </div>
      <div class="card-foot"><span class="tag-sale">Fore Sale</span><span class="tag-plus">+</span><span class="price">$192,00</span></div>
    </article>
    <article class="card">
      <div class="photo" role="img" aria-label="Photo of a cream house with a terracotta roof and garage" style="background:linear-gradient(180deg,#5f9fe0,#c0623a 45%,#e6dcc8 70%,#7a9a55)"></div>
      <h4>417 Linden Grove</h4>
      <div class="meta">
        <span><svg width="14" height="10"><rect x="1" y="4" width="12" height="5" fill="#666"/><rect x="1" y="1" width="4" height="3" fill="#666"/></svg>2 Bedrooms</span>
        <span><svg width="12" height="12"><rect x="1" y="1" width="10" height="10" fill="none" stroke="#666" stroke-width="1.5"/></svg>2198 sqft</span>
        <span><svg width="12" height="12"><path d="M1 6h10v3H1zM3 6V2h3" fill="none" stroke="#666" stroke-width="1.5"/></svg>4 baths</span>
        <span><svg width="14" height="10"><rect x="1" y="3" width="12" height="5" rx="2" fill="#666"/></svg>2 Car Garage</span>
      </div>
      <div class="card-foot"><span class="tag-sale">Fore Sale</span><span class="tag-plus">+</span><span class="price">$192,00</span></div>
    </article>
  </div>
</section>

<section class="block agents">
  <h2 class="section-title">OUR AGENT</h2>
  <article class="agent" style="left:131px;width:458px">
    <div class="portrait" role="img" aria-label="Portrait photo of agent Daniel Reeve" style="background:linear-gradient(180deg,#f4f4f4,#dfe3e8 60%,#c9ced6)"></div>
    <div class="agent-info">
      <h4>DANIEL REEVE</h4>
      <p>Lorem ipsum dolor sit amet, consectetur adipisicing elit, sed do eiusmod tempor incididunt ut labore et dolore magna aliqua</p>
      <div class="contact">Call: 0198765432<br>Mail: <em>d.reeve@larkfieldhomes.com</em></div>
    </div>
  </article>
  <article class="agent" style="left:607px;width:462px">
    <div class="portrait" role="img" aria-label="Portrait photo of agent Marcus Holloway" style="background:linear-gradient(180deg,#f6f6f6,#e8e4de 60%,#d6d2cc)"></div>
    <div class="agent-info">
      <h4>MARCUS HOLLOWAY</h4>
      <p>Lorem ipsum dolor sit amet, consectetur adipisicing elit, sed do eiusmod tempor incididunt ut labore et dolore magna aliqua</p>
      <div class="contact">Call: 0198765432<br>Mail: <em>m.holloway@larkfieldhomes.com</em></div>
    </div>
  </article>
</section>

<section class="block services">
  <div class="service" style="left:134px">
    <div class="icon active"><svg width="34" height="44"><path d="M17 2a14 14 0 0 0-14 14c0 11 14 26 14 26s14-15 14-26A14 14 0 0 0 17 2z" fill="#fff"/><circle cx="17" cy="16" r="6" fill="#1f1f1f"/></svg></div>
    <h3>Listing</h3>
    <p>Lorem ipsum dolor sit amet, consectetur adipisicing elit, sed do eiusmod tempor incididunt ut labore et dolore magna aliqua</p>
    <span class="btn-more">Read more &gt;</span>
  </div>
  <div class="service" style="left:453px">
    <div class="icon"><svg width="46" height="46"><circle cx="23" cy="23" r="12" fill="none" stroke="#8a8a8a" stroke-width="4"/><path d="M23 3v12M23 31v12M3 23h12M31 23h12" stroke="#8a8a8a" stroke-width="4"/></svg></div>
    <h3>Advertise</h3>
    <p>Lorem ipsum dolor sit amet, consectetur adipisicing elit, sed do eiusmod tempor incididunt ut labore et dolore magna aliqua</p>
    <span class="btn-more">Read more &gt;</span>
  </div>
  <div class="service" style="left:771px">
    <div class="icon"><svg width="50" height="26"><circle cx="12" cy="13" r="9" fill="none" stroke="#8a8a8a" stroke-width="5"/><path d="M21 13h26M40 13v8M47 13v8" stroke="#8a8a8a" stroke-width="5"/></svg></div>
    <h3>Guidance</h3>
    <p>Lorem ipsum dolor sit amet, consectetur adipisicing elit, sed do eiusmod tempor incididunt ut labore et dolore magna aliqua</p>
    <span class="btn-more">Read more &gt;</span>
  </div>
</section>

<footer class="block site-footer">
  <div class="col" style="left:131px">
    <h5>USEFUL LINKS</h5>
    <ul class="links"><li>HOME</li><li>SERVICES</li><li>HOME BUYERS</li><li>HOME SELLERS</li><li>TEAM</li><li>CONTACT</li></ul>
  </div>
  <div class="col" style="left:372px;width:220px">
    <h5>ABOUT US</h5>
    <p>Lorem ipsum dolor sit amet elit, consectetur adipiscing. Vestibulum luctus ipsum id quam euismod a malesuada sapien euismod. Vest ibulum ultricies elementum interdum.</p>
    <p class="more">Read more &gt;&gt;</p>
  </div>
  <div class="col" style="left:612px">
    <h5>FROM THE BLOG</h5>
    <div class="post"><div class="thumb" role="img" aria-label="Blog author photo" style="background:linear-gradient(180deg,#e2e2e2,#6a7a8c)"></div><p>Sed ut perspiciatis unde omnis iste natus error sit<small>22January 2012</small></p></div>
    <div class="post"><div class="thumb" role="img" aria-label="Blog author photo" style="background:linear-gradient(180deg,#eeeeee,#a98a7a)"></div><p>Sed ut perspiciatis unde omnis iste natus error sit<small>22January 2012</small></p></div>
  </div>
  <div class="col" style="left:850px;width:220px">
    <h5>CONTACT US</h5>
    <ul class="contact-list">
      <li><svg width="12" height="15"><path d="M6 1a5 5 0 0 0-5 5c0 4 5 8 5 8s5-4 5-8a5 5 0 0 0-5-5z" fill="#333"/></svg><span>No 18 Carver Lane 22/4 Maplewood City ,NJ United States</span></li>
      <li><svg width="13" height="11"><rect x="0.5" y="1" width="12" height="9" fill="#333"/><path d="M1 1.5l5.5 4 5.5-4" fill="none" stroke="#ddd"/></svg><span>hello@larkfieldhomes.com<br>sales@larkfieldhomes.com</span></li>
      <li><svg width="13" height="13"><path d="M2 1h3l1 3-2 1.5a7 7 0 0 0 3.5 3.5L9 7l3 1v3a1 1 0 0 1-1 1A10 10 0 0 1 1 2a1 1 0 0 1 1-1z" fill="#333"/></svg><span>(+80) 05523456-789<br>(+80) 05523456-789</span></li>
    </ul>
  </div>
</footer>

<div class="block site-bottom">
  <div class="copyright">Copyright © 2013 Company Name. All rights reserved.</div>
  <div class="social"><span></span><span></span><span></span><span></span><span></span></div>
  <div class="to-top"><svg width="40" height="22"><path d="M3 19L20 3l17 16" fill="none" stroke="#bbb" stroke-width="3"/></svg></div>
</div>

</body>
</html>
```